Bright Dune Series- Face & Body Oil Label

Hi,
I need a label design for a new brand- "Bright Dune Series". Modern and expensive looking. Any color scheme. Feel free to be creative! (I'm not set on the brand name above... I was also thinking maybe "LUXA" or "PuraGlow".
-Packaging: 4oz / 118mL clear glass "boston round" bottle with a white treatment pump. The product is an oil so it has a golden tint.
-Product: 4oz Biotin & Marula Face & Body Oil (note that the featured ingredients will change. Others will be "Rosehip & Vitamin E", "Lavender & Hemp Seed Oil", "Coconut Oil & Vitamin C"
-Label size: 5" x 2.5" rounded corners
-Main Highlight: "Moisturizing & Healing"
-Other Highlights:
-----non-greasy
-----all-natural
-----paraben-free
-----vegan
(feel free to use icon symbols)
-Ingredient deck attached
-Other info:
----made in Los Angeles, CA
----manufactured by Willowmark Blends LLC
----UPC
The main thing here is the logo and textures to the label. I can fill in / rearrange the info after.
Thank you,
Theo

```html
<!DOCTYPE html>
<html lang="en">
<head>
<meta charset="utf-8">
<title>Bright Dune Series – Face &amp; Body Oil Label</title>
<link rel="stylesheet" href="https://fonts.googleapis.com/css2?family=Dosis:wght@500;600&family=Tinos:wght@400;700&display=swap">
<style>
  :root {
    --backdrop: #8c8c8c;
    --label-black: #1c1c1c;
    --gold: #f2cf3a;
    --gold-light: #fff38a;
    --gold-deep: #e1ac17;
    --ink: #111111;
  }
  * { box-sizing: border-box; margin: 0; padding: 0; }
  html, body { width: 1034px; height: 1200px; overflow: hidden; }
  body {
    background: radial-gradient(circle at 50% 50%, #a9a9a9 0%, var(--backdrop) 70%);
    font-family: "Tinos", "Times New Roman", serif;
  }
  .label {
    position: absolute;
    left: 113px; top: 398px;
    width: 808px; height: 404px;
  }
  .label-shape { position: absolute; inset: 0; }
  .brand-name {
    position: absolute; left: 254px; top: 86px; width: 300px;
    text-align: center; color: var(--gold);
    font-family: "Dosis", "Arial", sans-serif; font-weight: 500;
    line-height: 1;
  }
  .brand-name .line-main { display: block; font-size: 40px; letter-spacing: 1px; }
  .brand-name .line-sub { display: block; font-size: 21px; letter-spacing: 2px; margin-top: 6px; }
  .product-title {
    position: absolute; left: 204px; top: 211px; width: 400px;
    text-align: center; color: var(--gold);
    font-family: "Dosis", "Arial", sans-serif; font-weight: 600;
    font-size: 25px; line-height: 28px;
  }
  .ingredients {
    position: absolute; left: 13px; top: 178px; width: 220px;
    text-align: center; color: var(--gold);
  }
  .ingredients .maker-heading {
    display: inline-block; font-weight: 700; font-size: 16px;
    letter-spacing: 0.3px; padding: 0 10px 2px;
    border-bottom: 1.5px solid var(--gold);
  }
  .ingredients .deck-heading { font-weight: 700; font-size: 12.5px; margin-top: 16px; }
  .ingredients ul { list-style: none; font-size: 11.5px; line-height: 15px; margin-top: 1px; }
  .maker-info {
    position: absolute; left: 582px; top: 100px; width: 220px;
    text-align: center; color: var(--gold); font-size: 11.5px; line-height: 15px;
  }
  .lab-mark { display: flex; flex-direction: column; align-items: center; gap: 8px; }
  .lab-mark .dot {
    width: 52px; height: 52px; border-radius: 50%;
    border: 2px solid var(--gold);
  }
  .lab-mark .lab-name {
    font-family: "Dosis", "Arial", sans-serif; font-weight: 500;
    font-size: 13px; letter-spacing: 0.5px;
  }
  .maker-info address { font-style: normal; margin-top: 14px; }
  .maker-info .origin { margin-top: 27px; }
  .maker-info strong { font-weight: 700; }
  .vegan-mark {
    position: absolute; left: 332px; top: 333px; width: 72px; height: 46px;
    border-radius: 8px; background: linear-gradient(90deg, #2a2a2a, #3b3b3b);
    opacity: 0.85;
  }
  .size-badge {
    position: absolute; left: 432px; top: 336px; width: 42px; height: 42px;
    border-radius: 50%; background: var(--ink); color: var(--gold);
    font-family: "Dosis", "Arial", sans-serif; font-weight: 500; font-size: 17px;
    display: flex; align-items: center; justify-content: center;
  }
</style>
</head>
<body>
  <section class="label">
    <svg class="label-shape" viewBox="0 0 808 404" aria-hidden="true">
      <defs>
        <linearGradient id="gold-band" x1="0" x2="1" y1="0" y2="0">
          <stop offset="0" stop-color="#f2c91f"/>
          <stop offset="0.45" stop-color="#fff48c"/>
          <stop offset="1" stop-color="#e0aa15"/>
        </linearGradient>
        <clipPath id="label-clip">
          <rect x="0" y="0" width="808" height="404" rx="24"/>
        </clipPath>
      </defs>
      <g clip-path="url(#label-clip)">
        <rect class="band-top" x="0" y="0" width="808" height="404" fill="url(#gold-band)"/>
        <path class="field-black" fill="#1c1c1c"
          d="M0 9 H808 V383 H600 Q557 383 557 345 Q557 318 530 318 H278 Q250 318 250 345 Q250 383 208 383 H0 Z"/>
        <rect x="0" y="365" width="232" height="3" rx="1.5" fill="url(#gold-band)"/>
        <rect x="575" y="365" width="240" height="3" rx="1.5" fill="url(#gold-band)"/>
      </g>
    </svg>

    <h1 class="brand-name">
      <span class="line-main">BRIGHT DUNE</span>
      <span class="line-sub">SERIES</span>
    </h1>

    <h2 class="product-title">Biotin &amp; Marula Face<br>&amp; Body Oil</h2>

    <div class="ingredients">
      <p class="maker-heading">WILLOWMARK BLENDS</p>
      <p class="deck-heading">INGREDIENT:</p>
      <ul>
        <li>Glycine Soja (Soybean) Oil</li>
        <li>Lavandula Angustifolia (Lavender) Oil</li>
        <li>Sclerocarya Birrea (Marula) Seed Oil</li>
        <li>Cannabis Sativa (Hemp) Seed Oil</li>
        <li>Persea Gratissima (Avocado) Oil</li>
        <li>Prunus Armenica (Apricot) Kernel Oil</li>
        <li>Tocopherol</li>
        <li>Fragrance (Parfum)</li>
      </ul>
    </div>

    <div class="maker-info">
      <div class="lab-mark">
        <span class="dot"></span>
        <span class="lab-name">FERNVALE LABS</span>
      </div>
      <address>
        4820 Marlow Ave., Reseda,<br>
        California 91335<br>
        P: 818-555-0142&nbsp; F: 818-555-0199<br>
        Website: www.solaceleaf.com
      </address>
      <p class="origin">made in <strong>Los Angeles, CA</strong><br>
        manufactured by Willowmark Blends LLC<br>UPC</p>
    </div>

    <div class="vegan-mark" role="img" aria-label="Hand-lettered Vegan script with small leaf"></div>
    <div class="size-badge">4oz</div>
  </section>
</body>
</html>
```